Fahrzeugbeschriftung für ambulanten Pflegedienst
Zielgruppe
Ambulanter Pflegedienst
(Bitte um deutsche Kommunikation)
Aufgabenstellung
Unser Logo und unser Motto, farbliche Komponenten, die wichtigste Leistungen, Mail Adresse, Flyer vorhanden, Fahrzeuge haben einen weißen Hintergrund. Es sind 3 Fahrzeug Modelle : Zipo Kleinflink Baujahr 2008, Norvak Reihe 5 Baujahr 2023 und KR Ilo 2 Türig Baujahr 2008, Kontaktdaten wie Telefonnummer und Mail Adresse müssen sichtlich sein.
Die Welle im Flyer soll auch auf den Fahrzeugen abgebildet sein.
Hierbei stellen wir uns folgendes vor:
Die zweifarbige Teilung, mit der Welle, soll sich von A - Säule bis C-Säule vollstrecken.
Abbildungen vom Flyer soll genutzt werden, z.B. Die Hand mit den Personen.
Ein Beispiel, für Auffälligkeit habe ich 3 Bilder von anderen Fahrzeugen beigefügt (nur als Beispiel)
Die Schrift 'Ambulanter Pflegedienst' muss betont sein.
Zu unseren Leistungen die aufgeführt werden müssen;
- Grundpflege
- Behandlungspflege
- Wundmanagement
- Pflegeberatung

```html
<!DOCTYPE html>
<html lang="de">
<head>
<meta charset="utf-8">
<title>Fahrzeugbeschriftung – Ambulanter Pflegedienst</title>
<link href="https://fonts.googleapis.com/css2?family=Poppins:wght@600;700;800&display=swap" rel="stylesheet">
<style>
  :root {
    --white: #ffffff;
    --page: #f3f4f5;
    --headline-blue: #1a6fb3;
    --ink: #1b1b1b;
    --wave-teal: #5cc0b9;
    --wave-blue-a: #00b3d6;
    --wave-blue-b: #1b9fe2;
    --tick-teal: #4fb39a;
    --illu-pink: #f2a99a;
    --illu-green: #3f9b78;
    --illu-blue: #4e8fd0;
  }
  html, body {
    margin: 0;
    width: 1200px;
    height: 1200px;
    overflow: hidden;
    background: var(--page);
    font-family: "Poppins", sans-serif;
  }
  .wrap-artwork {
    position: absolute;
    left: 40px;
    top: 240px;
    width: 1120px;
    height: 720px;
    background: var(--white);
    overflow: hidden;
    border-radius: 6px;
  }
  .wave-layer {
    position: absolute;
    inset: 0;
  }
  .headline {
    position: absolute;
    left: 90px;
    top: 70px;
    margin: 0;
    color: var(--headline-blue);
    font-weight: 800;
    font-size: 62px;
    line-height: 1.12;
    letter-spacing: 1px;
  }
  .services {
    position: absolute;
    left: 90px;
    top: 250px;
    margin: 0;
    padding: 0;
    list-style: none;
    color: var(--ink);
    font-weight: 700;
    font-size: 27px;
    line-height: 1.45;
    letter-spacing: 0.5px;
  }
  .services li {
    position: relative;
    padding-left: 48px;
  }
  .services li::before {
    content: "";
    position: absolute;
    left: 0;
    top: 13px;
    width: 14px;
    height: 14px;
    border-radius: 50%;
    background: var(--ink);
  }
  .care-illustration {
    position: absolute;
    left: 620px;
    top: 120px;
    width: 420px;
    height: 400px;
    border-radius: 46% 46% 40% 40%;
    background: linear-gradient(160deg, var(--illu-green) 0%, var(--illu-blue) 50%, var(--illu-pink) 100%);
    opacity: 0.85;
  }
  .tick-badge {
    position: absolute;
    left: 930px;
    top: 40px;
  }
  .contact-rule {
    position: absolute;
    left: 100px;
    top: 585px;
    width: 120px;
    height: 3px;
    background: var(--white);
  }
  .contact-mail {
    position: absolute;
    left: 100px;
    top: 615px;
    display: flex;
    flex-direction: column;
    gap: 10px;
    color: var(--white);
    font-weight: 600;
    font-size: 27px;
    letter-spacing: 1.5px;
  }
</style>
</head>
<body>
  <main class="wrap-artwork">
    <svg class="wave-layer" width="1120" height="720" viewBox="0 0 1120 720" aria-hidden="true">
      <defs>
        <linearGradient id="blueBand" x1="0" y1="0" x2="1" y2="0">
          <stop offset="0" stop-color="var(--wave-blue-a)"/>
          <stop offset="1" stop-color="var(--wave-blue-b)"/>
        </linearGradient>
      </defs>
      <path d="M0 220 C160 200 260 260 360 380 C460 500 620 520 760 420 C880 340 980 400 1120 420 L1120 720 L0 720 Z" fill="var(--wave-teal)"/>
      <path d="M0 250 C150 240 250 300 340 420 C440 540 640 560 800 470 C920 400 1000 440 1120 450 L1120 720 L0 720 Z" fill="url(#blueBand)"/>
      <path d="M1120 520 C1040 500 980 540 920 600 L900 720 L1120 720 Z" fill="var(--wave-teal)" opacity="0.8"/>
      <circle cx="70" cy="470" r="40" fill="var(--white)"/>
      <circle cx="150" cy="455" r="26" fill="var(--white)"/>
      <circle cx="220" cy="455" r="17" fill="var(--white)"/>
      <circle cx="270" cy="470" r="8" fill="var(--white)"/>
      <circle cx="1060" cy="460" r="7" fill="var(--white)"/>
      <circle cx="1020" cy="500" r="14" fill="var(--white)"/>
      <circle cx="970" cy="560" r="22" fill="var(--white)"/>
      <circle cx="950" cy="640" r="38" fill="var(--white)"/>
    </svg>

    <h1 class="headline">Ambulanter<br>Pflegedienst</h1>

    <ul class="services">
      <li>Grundpflege</li>
      <li>Behandlungspflege</li>
      <li>Wundmanagement</li>
      <li>Pflegeberatung § 37.3</li>
    </ul>

    <div class="care-illustration" role="img" aria-label="Illustration: eine offene Hand trägt eine Pflegekraft, eine Person im Rollstuhl und ein Kind"></div>

    <svg class="tick-badge" width="70" height="70" viewBox="0 0 70 70" aria-hidden="true">
      <circle cx="35" cy="35" r="30" fill="var(--tick-teal)" opacity="0.85"/>
      <path d="M20 36 L31 47 L52 22" fill="none" stroke="var(--illu-green)" stroke-width="8" stroke-linecap="round" stroke-linejoin="round"/>
    </svg>

    <div class="contact-rule"></div>
    <div class="contact-mail">
      <svg width="36" height="36" viewBox="0 0 36 36" aria-hidden="true">
        <circle cx="18" cy="18" r="18" fill="var(--white)"/>
        <rect x="9" y="12" width="18" height="12" rx="1.5" fill="var(--wave-blue-b)"/>
        <path d="M9.5 12.5 L18 19 L26.5 12.5" fill="none" stroke="var(--white)" stroke-width="1.6"/>
      </svg>
      <span>info@helfa-pflege.de</span>
    </div>
  </main>
</body>
</html>
```